Pull Up Banner and Corresponding Postcard

Pull up Banner:

We are participating in two upcoming trade shows and need a pull of banner created, size is approx. 79x35.25".

Our give away is a stress reliever in the shape of a puzzle piece and the color is a royal blue. On one side it will say
Missing Something?
We can help.

The colors need to match our color palette with the blue mixed in that is prevalent in our website and also to tie in to the puzzle piece we are giving away.

Bramwick Logo on Top of Banner

Under logo:
Missing Something?
We can help.

Design in middle should mirror a puzzle with a missing piece. I've attached an example, however it should tie in to our colors.

Bottom:
-Modernize Business Processes
-Define and Implement Systems
-Automate and Manage Workflow
-Align, Prioritize, and Focus Efforts
-Execute, Execute, Execute

BramwickConsulting.com

Post Card:
Size 4.25 X 6": 2 Sided Color

Front Side:
Missing Something?
We can help.

Puzzle Image in Back for recognition

Wording: (see design of business card as well)

If it fits: Quote from Website: Dale Porrows quote from website: http://www.bramwickconsulting.com/vision/

Logo (2-Line Tagline)
Address: 4127 Gallery Loop, Reno NV 89533
775.618.2947

Note: I'm open to the content being moved around where it makes the most sense.

Quellbridge Certified Consultant Logo
Updates

An example of what a pull up banner is has been added (see Quellbridge banner- screen shot)

Target Market(s)

Small business owners 1-15 million

Industry/Entity Type

Trade

Requirements
Must have
• -Must match color palette/branding
-Banner: Middle should be uncluttered, words on top and bottom, visual in the middle
-Postcard and Banner should tie together for recognition purposes

NOTE: Some changes will be made on the website, including the addition of a new accent color (plum) for call to actions. Look should be more vibrant than the website.
Nice to have
• - Wording for fonts:
Ariel or Calibri to match business cards
Should not have
• Should Not Have:
- Banner with missing piece is not the exact image I want as the colors are off.

For an additional accent piece (secondary level), use Quellbridge Green. I can get you the exact color if you want to use it.

I attached an example of the business card- it is printed on white.

```html
<!DOCTYPE html>
<html lang="en">
<head>
<meta charset="utf-8">
<title>Choose Back – Bramwick Consulting Group Postcard</title>
<link rel="stylesheet" href="https://fonts.googleapis.com/css2?family=Roboto+Condensed:wght@700&family=Carlito:wght@400;700&family=Cormorant+SC:wght@500&display=swap">
<style>
  :root {
    --heading-blue: #3a6593;
    --brand-red: #93233a;
    --brand-brown: #4a2518;
    --rule-grey: #b3b3b3;
    --card-border: #333333;
    --paper: #ffffff;
  }
  * { box-sizing: border-box; margin: 0; padding: 0; }
  html, body {
    width: 1200px; height: 1000px; overflow: hidden;
    background: var(--paper);
  }
  body {
    position: relative;
    font-family: "Carlito", Calibri, sans-serif;
  }
  .page-title {
    position: absolute; top: 58px; left: 0; width: 1200px;
    text-align: center;
    font-family: "Roboto Condensed", "Arial Narrow", sans-serif;
    font-weight: 700; font-size: 68px; letter-spacing: -1px;
    color: var(--heading-blue);
  }
  .postcard {
    position: absolute; width: 570px; height: 380px;
    border: 1px solid var(--card-border);
    background: var(--paper);
    overflow: hidden;
  }
  .postcard--one { left: 12px; top: 170px; }
  .postcard--two { left: 609px; top: 170px; }
  .postcard--three { left: 327px; top: 566px; }

  .brand {
    position: absolute; left: 20px; top: 14px;
    display: flex; align-items: center; gap: 6px;
  }
  .brand__mark { width: 10px; height: 10px; background: var(--brand-brown); flex: none; }
  .brand__name {
    font-size: 18px; font-weight: 700; line-height: 1;
    color: var(--brand-brown);
  }

  .return-address {
    position: absolute; left: 403px; top: 11px;
    font-size: 11.5px; line-height: 14px; color: var(--brand-red);
    font-style: normal;
  }
  .return-address__line { padding-left: 11px; position: relative; }
  .return-address__pin { position: absolute; left: 0; top: 3px; width: 8px; height: 9px; }

  .divider {
    position: absolute; left: 284px; width: 2px; height: 252px;
    background: var(--brand-red);
  }
  .address-panel { position: absolute; left: 300px; top: 74px; width: 227px; }
  .address-panel__label { font-size: 15px; color: var(--brand-red); line-height: 20px; }
  .address-panel__rule { height: 1px; background: var(--rule-grey); margin-top: 25px; }
  .address-panel__rule--first { margin-top: 19px; }
  .address-panel__rule--after-note { margin-top: 18px; }
  .address-panel__label--note { margin-top: 22px; }

  .contact-band {
    position: absolute; left: 0; bottom: 0; width: 100%; height: 54px;
    background: var(--brand-red); color: var(--paper);
  }
  .contact-list { position: absolute; left: 20px; top: 5px; list-style: none; }
  .contact-list__item {
    font-size: 11px; line-height: 12.3px; display: flex; align-items: center; gap: 4px;
  }
  .contact-list__icon { width: 9px; height: 9px; flex: none; }
  .band-slogan {
    position: absolute; right: 10px; top: 7px; text-align: right;
    font-family: "Cormorant SC", Georgia, serif; font-weight: 500;
    font-size: 17px; line-height: 21px; color: var(--paper);
  }
  .band-slogan__second { padding-right: 20px; }
</style>
</head>
<body>
  <h1 class="page-title">Choose Back</h1>

  <section class="postcard postcard--one">
    <div class="brand"><span class="brand__mark"></span><span class="brand__name">Bramwick</span></div>
    <address class="return-address">
      <div class="return-address__line">Bramwick Consulting Group</div>
      <div class="return-address__line"><svg class="return-address__pin" viewBox="0 0 8 9"><circle cx="4" cy="4" r="3.4" fill="none" stroke="#93233a" stroke-width="1"/><circle cx="4" cy="4" r="1.2" fill="#93233a"/></svg>4127 Gallery Loop, Ste. 116</div>
      <div class="return-address__line">Reno, NV 89533</div>
    </address>
    <div class="divider" style="top:62px"></div>
    <div class="address-panel">
      <p class="address-panel__label">Send to:</p>
      <div class="address-panel__rule address-panel__rule--first"></div>
      <div class="address-panel__rule"></div>
      <div class="address-panel__rule"></div>
      <div class="address-panel__rule"></div>
      <p class="address-panel__label address-panel__label--note">Please add personal note:</p>
      <div class="address-panel__rule address-panel__rule--after-note"></div>
      <div class="address-panel__rule"></div>
      <div class="address-panel__rule"></div>
    </div>
    <footer class="contact-band">
      <ul class="contact-list">
        <li class="contact-list__item"><svg class="contact-list__icon" viewBox="0 0 10 10"><circle cx="5" cy="5" r="4.4" fill="none" stroke="#fff"/><path d="M3.3 2.6l1 1-.5.7c.3.6.8 1.1 1.4 1.4l.7-.5 1 1-.7.8C4.7 7 3 5.3 2.6 3.3z" fill="#fff"/></svg>775.618.2947</li>
        <li class="contact-list__item"><svg class="contact-list__icon" viewBox="0 0 10 10"><circle cx="5" cy="5" r="4.8" fill="#fff"/><rect x="2.4" y="3.3" width="5.2" height="3.4" fill="#93233a"/><path d="M2.4 3.3L5 5.2l2.6-1.9" stroke="#fff" stroke-width=".6" fill="none"/></svg>Connect@BramwickConsulting.com</li>
        <li class="contact-list__item"><svg class="contact-list__icon" viewBox="0 0 10 10"><circle cx="5" cy="5" r="4.4" fill="none" stroke="#fff"/><ellipse cx="5" cy="5" rx="1.9" ry="4.4" fill="none" stroke="#fff" stroke-width=".7"/><path d="M.6 5h8.8" stroke="#fff" stroke-width=".7"/></svg>www.BramwickConsulting.com</li>
      </ul>
      <p class="band-slogan">Missing Something?<br><span class="band-slogan__second">We Can Help.</span></p>
    </footer>
  </section>

  <section class="postcard postcard--two">
    <div class="brand"><span class="brand__mark"></span><span class="brand__name">Bramwick</span></div>
    <address class="return-address" style="top:9px">
      <div class="return-address__line">Bramwick Consulting Group</div>
      <div class="return-address__line"><svg class="return-address__pin" viewBox="0 0 8 9"><circle cx="4" cy="4" r="3.4" fill="none" stroke="#93233a" stroke-width="1"/><circle cx="4" cy="4" r="1.2" fill="#93233a"/></svg>4127 Gallery Loop, Ste. 116</div>
      <div class="return-address__line">Reno, NV 89533</div>
    </address>
    <div class="divider" style="top:64px"></div>
    <div class="address-panel" style="top:76px">
      <p class="address-panel__label">Send to:</p>
      <div class="address-panel__rule address-panel__rule--first"></div>
      <div class="address-panel__rule"></div>
      <div class="address-panel__rule"></div>
      <div class="address-panel__rule"></div>
      <p class="address-panel__label address-panel__label--note" style="margin-top:20px">Please add personal note:</p>
      <div class="address-panel__rule address-panel__rule--after-note"></div>
      <div class="address-panel__rule"></div>
      <div class="address-panel__rule"></div>
    </div>
    <footer class="contact-band">
      <ul class="contact-list">
        <li class="contact-list__item"><svg class="contact-list__icon" viewBox="0 0 10 10"><circle cx="5" cy="5" r="4.4" fill="none" stroke="#fff"/><path d="M3.3 2.6l1 1-.5.7c.3.6.8 1.1 1.4 1.4l.7-.5 1 1-.7.8C4.7 7 3 5.3 2.6 3.3z" fill="#fff"/></svg>775.618.2947</li>
        <li class="contact-list__item"><svg class="contact-list__icon" viewBox="0 0 10 10"><circle cx="5" cy="5" r="4.8" fill="#fff"/><rect x="2.4" y="3.3" width="5.2" height="3.4" fill="#93233a"/><path d="M2.4 3.3L5 5.2l2.6-1.9" stroke="#fff" stroke-width=".6" fill="none"/></svg>Connect@BramwickConsulting.com</li>
        <li class="contact-list__item"><svg class="contact-list__icon" viewBox="0 0 10 10"><circle cx="5" cy="5" r="4.4" fill="none" stroke="#fff"/><ellipse cx="5" cy="5" rx="1.9" ry="4.4" fill="none" stroke="#fff" stroke-width=".7"/><path d="M.6 5h8.8" stroke="#fff" stroke-width=".7"/></svg>www.BramwickConsulting.com</li>
      </ul>
    </footer>
  </section>

  <section class="postcard postcard--three">
    <div class="brand"><span class="brand__mark"></span><span class="brand__name">Bramwick</span></div>
    <address class="return-address" style="top:9px">
      <div class="return-address__line">Bramwick Consulting Group</div>
      <div class="return-address__line"><svg class="return-address__pin" viewBox="0 0 8 9"><circle cx="4" cy="4" r="3.4" fill="none" stroke="#93233a" stroke-width="1"/><circle cx="4" cy="4" r="1.2" fill="#93233a"/></svg>4127 Gallery Loop, Ste. 116</div>
      <div class="return-address__line">Reno, NV 89533</div>
    </address>
    <div class="divider" style="top:64px"></div>
    <footer class="contact-band" style="height:51px">
      <ul class="contact-list" style="top:4px">
        <li class="contact-list__item"><svg class="contact-list__icon" viewBox="0 0 10 10"><circle cx="5" cy="5" r="4.4" fill="none" stroke="#fff"/><path d="M3.3 2.6l1 1-.5.7c.3.6.8 1.1 1.4 1.4l.7-.5 1 1-.7.8C4.7 7 3 5.3 2.6 3.3z" fill="#fff"/></svg>775.618.2947</li>
        <li class="contact-list__item"><svg class="contact-list__icon" viewBox="0 0 10 10"><circle cx="5" cy="5" r="4.8" fill="#fff"/><rect x="2.4" y="3.3" width="5.2" height="3.4" fill="#93233a"/><path d="M2.4 3.3L5 5.2l2.6-1.9" stroke="#fff" stroke-width=".6" fill="none"/></svg>Connect@BramwickConsulting.com</li>
        <li class="contact-list__item"><svg class="contact-list__icon" viewBox="0 0 10 10"><circle cx="5" cy="5" r="4.4" fill="none" stroke="#fff"/><ellipse cx="5" cy="5" rx="1.9" ry="4.4" fill="none" stroke="#fff" stroke-width=".7"/><path d="M.6 5h8.8" stroke="#fff" stroke-width=".7"/></svg>www.BramwickConsulting.com</li>
      </ul>
    </footer>
  </section>
</body>
</html>
```